Photography Price List DL flyer

In need of a double sided DL flyer to list prices for a photography business that is in the real estate industry. Will need to include logo and be themed to match. Price details and contact information are in the pdf attached.

Below are links to the logo and photos that can be used on the flyer.

Logo
https://www.filquarry.net/s/tmewqoral7bnzx/LogoFiles.zip?dl=0

Photos
https://www.filquarry.net/s/p3vhnkelo81rtw/Website_Images.zip?dl=0

Sorry people the photo examples I put the wrong link. I have fixed it in the brief but the proper link is: https://www.filquarry.net/s/p3vhnkelo81rtw/Website_Images.zip?dl=0

Also dimensions of a DL are 210mm x 99mm + 3m bleed. Thanks

Target Market(s)

Real estate agents

Industry/Entity Type

Business

Requirements
Must have
• Price lists and contact information

```html
<!DOCTYPE html>
<html lang="en">
<head>
<meta charset="utf-8">
<title>Brightframe Photos – Price List</title>
<link rel="stylesheet" href="https://fonts.googleapis.com/css2?family=Tinos&display=swap">
<style>
  :root {
    --paper: #ffffff;
    --charcoal: #3a3a3a;
    --rose: #cd6b6a;
    --font-serif: "Tinos", "Times New Roman", serif;
  }
  * { margin: 0; padding: 0; box-sizing: border-box; }
  html, body { width: 1200px; height: 2468px; overflow: hidden; background: var(--paper); }
  .flyer { position: relative; width: 1200px; height: 2468px; background: var(--paper); font-family: var(--font-serif); color: var(--rose); }

  .brand-band { position: absolute; left: 58px; top: 52px; width: 1084px; height: 264px; background: var(--charcoal); display: flex; align-items: center; justify-content: center; gap: 40px; }
  .brand-name { font-size: 60px; letter-spacing: 4px; color: var(--rose); white-space: nowrap; }
  .brand-dot { width: 150px; height: 150px; border-radius: 50%; background: var(--rose); }

  .photo { position: absolute; }
  .photo--outdoor-kitchen { left: 58px; top: 406px; width: 1084px; height: 440px; background: linear-gradient(180deg, #8fa9c4 0%, #b7a89a 40%, #9a8674 70%, #c8a27f 100%); }
  .photo--deck { left: 58px; top: 955px; width: 670px; height: 503px; background: linear-gradient(180deg, #e5e7e6 0%, #8fae6f 35%, #5f7f48 60%, #3f4a55 100%); }
  .photo--dining { left: 60px; top: 1522px; width: 670px; height: 490px; background: linear-gradient(180deg, #f2f2f2 0%, #dcdcdc 45%, #b79a78 75%, #e8e8e8 100%); }

  .price-panel { position: absolute; left: 751px; top: 955px; width: 391px; height: 1150px; background: var(--charcoal); }
  .price-panel__title { position: absolute; top: 30px; width: 100%; text-align: center; font-size: 64px; font-weight: 400; }
  .price-group { position: absolute; left: 35px; }
  .price-group__heading { font-size: 52px; font-weight: 400; line-height: 1.1; }
  .price-group__item { font-size: 38px; line-height: 54px; white-space: nowrap; }
  .price-group--photo { top: 195px; }
  .price-group--twilight { top: 460px; }
  .price-group--floor { top: 696px; left: 32px; }
  .price-group--video { top: 828px; }

  .contact-band { position: absolute; left: 58px; top: 2105px; width: 1084px; height: 303px; background: var(--charcoal); padding: 24px 0 0 225px; }
  .contact-band__title { font-size: 54px; font-weight: 400; line-height: 66px; }
  .contact-band__line { font-size: 50px; line-height: 70px; white-space: nowrap; }
</style>
</head>
<body>
<main class="flyer">
  <header class="brand-band">
    <span class="brand-name">BRIGHTFRAME PHOTOS</span>
    <span class="brand-dot" aria-hidden="true"></span>
  </header>

  <div class="photo photo--outdoor-kitchen" role="img" aria-label="Photo of an outdoor kitchen and pool terrace with sun loungers at dusk"></div>
  <div class="photo photo--deck" role="img" aria-label="Photo of a covered timber deck with dining table overlooking leafy trees"></div>
  <div class="photo photo--dining" role="img" aria-label="Photo of a bright open-plan dining area and kitchen with tall windows"></div>

  <section class="price-panel">
    <h2 class="price-panel__title">Prices</h2>
    <div class="price-group price-group--photo">
      <h3 class="price-group__heading">Photography</h3>
      <p class="price-group__item">10 images&nbsp; $149</p>
      <p class="price-group__item">12-15 images $179</p>
      <p class="price-group__item">20 images $229</p>
    </div>
    <div class="price-group price-group--twilight">
      <h3 class="price-group__heading">Twilight</h3>
      <p class="price-group__item">Add $100 to image</p>
      <p class="price-group__item">package</p>
    </div>
    <div class="price-group price-group--floor">
      <p class="price-group__item">Floor plans - $49</p>
    </div>
    <div class="price-group price-group--video">
      <h3 class="price-group__heading">video</h3>
      <p class="price-group__item">30 seconds $150</p>
      <p class="price-group__item">60 seconds $200</p>
      <p class="price-group__item">2 minutes&nbsp;&nbsp; $300</p>
    </div>
  </section>

  <footer class="contact-band">
    <h2 class="contact-band__title">Contact Details</h2>
    <p class="contact-band__line">mobile : 0400 555 017</p>
    <p class="contact-band__line">web : brightframephotos .com.au</p>
    <p class="contact-band__line">email : info@brightframephotos.com.au</p>
  </footer>
</main>
</body>
</html>
```